Health Coach needs a Business Card Design

Need a really modern feminine business card design for a health and lifestyle coach. Needs to use geometric shapes, muted grey/blue/green pastels and black and white - see mood board attached and logo. The client likes black and white, modern, san serif with the use of lines and possibly a shadow leaf as in the mood board. Possibly put the tag line on the back or an icon of the logo. Logo is also attached. An icon of the logo would be great too.

Target Market(s)

Women (some men) aged 30 to 50.

Industry/Entity Type

Business

Contact Information for Business Card

Marla Teveny
e-mail: hello@marlatwell.example
website: marlatwell.example
Phone: +610497258316

The tag line is "Steady strength, every day"

Font styles to use
Sans Serif

Colors
ecf7fb
cfeae6
000000
ffffff
f5f5f5

Requirements
Must have
• Black and white, logo, tag line and details
Nice to have
• Would be nice to incorporate the shadow palm.fern leaves as in the mood board and or geometric lines/shapes - see mood board. Could be either standard rectangle or would be happy with square too.
Should not have
• Flowers or decorations

```html
<!DOCTYPE html>
<html lang="en">
<head>
<meta charset="utf-8">
<title>Marla T — Business Card</title>
<link rel="stylesheet" href="https://fonts.googleapis.com/css2?family=Josefin+Sans:wght@300;400&display=swap">
<style>
  :root {
    --page: #a9e3d6;
    --card-white: #ffffff;
    --card-mint: #b7ddd5;
    --ink: #2b2f2f;
    --ink-soft: #5d6665;
    --sky: #ddebf3;
    --pale: #e6f2f3;
    --teal: #93cdc0;
    --mist: #f5f5f5;
    --rule: #9aa3a2;
  }
  * { box-sizing: border-box; margin: 0; padding: 0; }
  html, body {
    width: 1200px; height: 800px; overflow: hidden;
    background: var(--page);
    font-family: "Josefin Sans", sans-serif;
    color: var(--ink);
  }
  .sheet {
    position: relative; width: 1200px; height: 800px;
    display: flex; align-items: center; justify-content: center; gap: 60px;
  }
  .card {
    position: relative; width: 520px; height: 316px; overflow: hidden;
    box-shadow: 0 14px 30px rgba(40, 90, 80, 0.18);
  }
  .card-front { background: var(--card-white); }
  .card-back { background: var(--card-mint); }
  .card-shapes { position: absolute; inset: 0; width: 100%; height: 100%; }

  .brand {
    position: absolute; display: flex; align-items: center; gap: 10px;
    font-weight: 300; color: var(--ink); letter-spacing: 0.04em;
  }
  .brand-dot { display: block; border-radius: 50%; background: var(--teal); flex: none; }

  .card-front .brand { top: 34px; left: 40px; font-size: 24px; }
  .card-front .brand-dot { width: 12px; height: 12px; }

  .card-back .brand { top: 110px; left: 50px; font-size: 48px; }
  .card-back .brand-dot { width: 20px; height: 20px; background: var(--card-white); }

  .tagline {
    position: absolute; left: 50px; bottom: 56px;
    font-size: 15px; font-weight: 300; letter-spacing: 0.06em; color: var(--ink-soft);
  }

  .person { position: absolute; left: 40px; top: 136px; }
  .person-name {
    font-size: 20px; font-weight: 300; text-transform: uppercase;
    letter-spacing: 0.22em; margin-bottom: 16px;
  }
  .contact-list { list-style: none; }
  .contact-item {
    display: flex; align-items: center; gap: 12px;
    font-size: 12px; font-weight: 300; letter-spacing: 0.1em;
    color: var(--ink-soft); margin-bottom: 9px;
  }
  .contact-icon { width: 15px; height: 15px; flex: none; }
</style>
</head>
<body>
<main class="sheet">

  <section class="card card-front" aria-label="Business card front">
    <svg class="card-shapes" viewBox="0 0 520 316" aria-hidden="true">
      <rect x="388" y="0" width="132" height="316" fill="var(--sky)"/>
      <rect x="420" y="200" width="64" height="64" fill="var(--teal)"/>
      <rect x="360" y="60" width="60" height="60" fill="var(--mist)"/>
      <line x1="40" y1="104" x2="340" y2="104" stroke="var(--rule)" stroke-width="0.75"/>
      <line x1="420" y1="40" x2="520" y2="40" stroke="var(--card-white)" stroke-width="1"/>
      <line x1="420" y1="52" x2="520" y2="52" stroke="var(--card-white)" stroke-width="1"/>
    </svg>

    <div class="brand"><span class="brand-dot"></span>Marla T</div>

    <div class="person">
      <h1 class="person-name">Marla Teveny</h1>
      <ul class="contact-list">
        <li class="contact-item">
          <svg class="contact-icon" viewBox="0 0 16 16" aria-hidden="true"><rect x="1.5" y="3.5" width="13" height="9" fill="none" stroke="var(--ink)"/><path d="M1.5,3.5 L8,9 L14.5,3.5" fill="none" stroke="var(--ink)"/></svg>
          hello@marlatwell.example
        </li>
        <li class="contact-item">
          <svg class="contact-icon" viewBox="0 0 16 16" aria-hidden="true"><circle cx="8" cy="8" r="6.5" fill="none" stroke="var(--ink)"/><ellipse cx="8" cy="8" rx="3" ry="6.5" fill="none" stroke="var(--ink)"/><path d="M1.5,8 H14.5" stroke="var(--ink)"/></svg>
          marlatwell.example
        </li>
        <li class="contact-item">
          <svg class="contact-icon" viewBox="0 0 16 16" aria-hidden="true"><rect x="4.5" y="1.5" width="7" height="13" rx="1" fill="none" stroke="var(--ink)"/><line x1="7" y1="12" x2="9" y2="12" stroke="var(--ink)"/></svg>
          +610497258316
        </li>
      </ul>
    </div>
  </section>

  <section class="card card-back" aria-label="Business card back">
    <svg class="card-shapes" viewBox="0 0 520 316" aria-hidden="true">
      <rect x="360" y="0" width="160" height="316" fill="var(--pale)" opacity="0.55"/>
      <rect x="400" y="40" width="80" height="80" fill="none" stroke="var(--card-white)" stroke-width="2"/>
      <line x1="50" y1="220" x2="330" y2="220" stroke="var(--ink)" stroke-width="0.75"/>
    </svg>
    <div class="brand"><span class="brand-dot"></span>Marla T</div>
    <p class="tagline">Steady strength, every day</p>
  </section>

</main>
</body>
</html>
```